Simple but elegant business card/logo design for exclusive beauty business

We need a logo designed for a new elegant and exclusive beauty business called "G". The logo itself should be a stylistic and custom design for the letter "G". We would like the business card to have the logo as the centrepiece on a clean background. Gold Logo on black background or silver on white background.

The business card details should be displayed centre of the card. Details are as follows:

Tamsin Rowe
Facebook: /simplyshinebyr
Instagram: /simplyshinebyr

The words "Simply Shine" should also appear somewhere on the card.

G

• Design must be simple, clean and elegant
• The design should not be cluttered

```html
<!DOCTYPE html>
<html lang="en">
<head>
<meta charset="utf-8">
<title>Tamsin Rowe — Business Card</title>
<link rel="stylesheet" href="https://fonts.googleapis.com/css2?family=Cinzel:wght@400;500&family=Montserrat:wght@600&display=swap">
<style>
  :root {
    --frame-purple: #3a1545;
    --card-black: #000000;
    --gold-light: #e8c33a;
    --gold-mid: #c8991a;
    --gold-deep: #9a6e10;
    --accent-pink: #e0607e;
    --text-white: #ffffff;
  }
  html, body {
    margin: 0;
    padding: 0;
    width: 1200px;
    height: 708px;
    overflow: hidden;
    background: var(--frame-purple);
  }
  .card {
    position: relative;
    width: 1200px;
    height: 708px;
    overflow: hidden;
    background: var(--frame-purple);
  }
  .card-face {
    position: absolute;
    left: 24px;
    top: 24px;
    width: 1152px;
    height: 659px;
    background: var(--card-black);
  }
  .decor {
    position: absolute;
    inset: 0;
    width: 1200px;
    height: 708px;
  }
  .glitter-blob { fill: url(#goldGlitter); }
  .pink-blob { fill: var(--accent-pink); }
  .brand-mark {
    position: absolute;
    left: 810px;
    top: 250px;
    width: 310px;
    text-align: center;
    font-family: "Cinzel", serif;
    font-weight: 500;
    font-size: 60px;
    line-height: 1.15;
    color: var(--text-white);
    letter-spacing: 2px;
  }
  .contact {
    position: absolute;
    left: 33px;
    top: 466px;
    color: var(--text-white);
  }
  .contact-name {
    margin: 0;
    font-family: "Cinzel", serif;
    font-weight: 400;
    font-size: 92px;
    line-height: 1;
    letter-spacing: 3px;
  }
  .contact-links {
    list-style: none;
    margin: 18px 0 0;
    padding: 0;
    font-family: "Montserrat", sans-serif;
    font-weight: 600;
    font-size: 28px;
    letter-spacing: 0.5px;
  }
  .contact-links li { height: 52px; line-height: 52px; }
</style>
</head>
<body>
<div class="card">
  <div class="card-face"></div>

  <svg class="decor" viewBox="0 0 1098 648" preserveAspectRatio="none" role="img" aria-label="Gold glitter cloud shape with pink glitter accents behind it">
    <defs>
      <radialGradient id="goldGlitter" cx="60%" cy="45%" r="70%">
        <stop offset="0%" stop-color="var(--gold-light)"/>
        <stop offset="60%" stop-color="var(--gold-mid)"/>
        <stop offset="100%" stop-color="var(--gold-deep)"/>
      </radialGradient>
    </defs>
    <path class="pink-blob" d="M650 22 C660 5 700 0 720 0 L830 0 C835 20 825 40 810 50 L660 50 C645 45 645 30 650 22 Z"/>
    <path class="pink-blob" d="M1070 60 L1098 55 L1098 525 L1070 530 Z"/>
    <path class="pink-blob" d="M870 620 C900 598 960 595 1000 605 C1030 610 1045 630 1040 648 L880 648 C868 640 865 630 870 620 Z"/>
    <path class="glitter-blob" d="M640 25 C700 20 720 45 760 30 C800 20 850 35 900 40 L1050 45 L1098 60 L1098 520 C1060 530 1050 560 1030 600 C1000 640 950 630 900 620 L880 648 L680 648 C660 620 670 590 640 570 C600 560 620 520 600 500 C580 470 620 440 600 420 C590 400 570 390 560 370 C540 340 500 310 470 300 C450 290 455 250 475 235 C470 200 460 150 490 130 C520 110 560 100 600 90 C610 60 620 30 640 25 Z"/>
  </svg>

  <div class="brand-mark">Simply<br>Shine</div>

  <div class="contact">
    <h1 class="contact-name">TAMSIN ROWE</h1>
    <ul class="contact-links">
      <li>FACEBOOK.COM/SIMPLYSHINEBYR</li>
      <li>INSTAGRAM.COM/SIMPLYSHINEBYR</li>
    </ul>
  </div>
</div>
</body>
</html>
```